Modern church envelopes in which meme ears give donations for different ministries

create a modern envelope with current logo. It would have lines for name address etc. It should also have our website and Facebook page.

Industry/Entity Type

Church

Colors
ffcf3e
757575

Requirements
Must have
• logo, logo color scheme including black, the following lines:
• Name/Nombre , address/, email, phone, Tithe/Diezmo, offering/ofrenda, Missions/misiones, Building fund/construcion, special offering/ofrenda especial.
• Ways to give: cash or check with this envelope (for credit cards you may use the credit card form and insert into this envelope)
• online www.Vidanuevatx.com

```html
<!DOCTYPE html>
<html lang="en">
<head>
<meta charset="utf-8">
<title>Vida Nueva Mission Church – Giving Envelope</title>
<link rel="stylesheet" href="https://fonts.googleapis.com/css2?family=Cinzel:wght@400;700&family=Lato:wght@400;700&family=Arimo&display=swap">
<style>
  :root {
    --backdrop: #e4e4e4;
    --gold: #c9a24a;
    --grey: #757575;
    --ink: #1e1e1e;
    --paper: #ffffff;
    --rule: #b5b5b5;
    --night-top: #4a4a4a;
    --night-bottom: #000000;
  }
  * { box-sizing: border-box; margin: 0; padding: 0; }
  html, body { width: 1200px; height: 1200px; overflow: hidden; }
  body { background: var(--backdrop); position: relative; font-family: "Lato", sans-serif; color: var(--ink); }

  /* Front of envelope */
  .envelope-front {
    position: absolute; left: 154px; top: 82px; width: 893px; height: 498px;
    overflow: hidden;
  }
  .front-backdrop {
    position: absolute; inset: 0;
    background: linear-gradient(180deg, var(--night-top) 0%, #1a1a1a 45%, #0b0b0b 75%, var(--night-bottom) 100%);
  }
  .front-wordmark {
    position: absolute; left: 0; right: 0; top: 240px; text-align: center;
  }
  .front-wordmark .church-name {
    font-family: "Cinzel", serif; font-weight: 700; font-size: 58px; color: var(--gold); letter-spacing: 1px; line-height: 1;
  }
  .front-wordmark .church-sub {
    display: inline-flex; align-items: center; gap: 8px; margin-top: 6px;
    font-family: "Cinzel", serif; font-weight: 700; font-size: 15px; color: var(--paper);
  }
  .front-wordmark .church-sub::before,
  .front-wordmark .church-sub::after { content: ""; width: 64px; height: 2px; background: var(--paper); }
  .front-contact {
    position: absolute; left: 0; right: 0; top: 419px; text-align: center;
    color: var(--paper); font-weight: 700; font-size: 19px; letter-spacing: 0.6px; line-height: 28px;
  }
  .divider-bar { display: inline-block; width: 2px; height: 20px; background: currentColor; vertical-align: -3px; margin: 0 8px; }

  /* Back of envelope */
  .envelope-back {
    position: absolute; left: 154px; top: 619px; width: 893px; height: 499px; background: var(--paper);
  }
  .back-frame {
    position: absolute; left: 10px; top: 11px; width: 872px; height: 476px; border: 2px solid var(--rule);
  }
  .back-header-rule { position: absolute; left: 10px; top: 136px; width: 872px; height: 2px; background: var(--rule); }
  .back-column-rule { position: absolute; left: 521px; top: 137px; width: 2px; height: 350px; background: var(--rule); }

  .back-wordmark { position: absolute; left: 58px; top: 46px; width: 160px; text-align: center; }
  .back-wordmark .church-name { font-family: "Cinzel", serif; font-weight: 700; font-size: 28px; color: var(--gold); line-height: 1; }
  .back-wordmark .church-sub { font-family: "Cinzel", serif; font-weight: 700; font-size: 10px; color: var(--grey); margin-top: 4px; }

  .mission-statement {
    position: absolute; left: 268px; top: 33px; width: 592px;
    font-size: 13px; line-height: 16px; font-weight: 700; letter-spacing: 0.5px; text-align: justify; color: #2a2a2a;
  }

  .donor-form { font-family: "Arimo", sans-serif; font-size: 14.5px; color: var(--ink); }
  .form-row { position: absolute; left: 60px; display: flex; align-items: flex-end; gap: 6px; }
  .form-line { border-bottom: 1px solid var(--ink); height: 14px; }

  .back-contact {
    position: absolute; left: 10px; width: 512px; top: 413px; text-align: center;
    font-weight: 700; font-size: 15px; letter-spacing: 0.5px; line-height: 23px;
  }
  .back-contact .divider-bar { height: 17px; margin: 0 6px; }

  .ways-to-give { position: absolute; left: 540px; top: 148px; width: 322px; text-align: center; }
  .ways-title { font-family: "Cinzel", serif; font-size: 38px; line-height: 1; letter-spacing: 0.5px; }
  .ways-sub { font-family: "Cinzel", serif; font-size: 12px; margin-top: 4px; color: #333; }
  .ways-rule { height: 1px; margin: 6px 20px 0 10px; background: linear-gradient(90deg, #999, #ccc 80%, transparent); }

  .gift-options { position: absolute; left: 542px; top: 216px; list-style: none; font-family: "Arimo", sans-serif; font-size: 19px; }
  .gift-options li { display: flex; align-items: center; gap: 10px; height: 29.5px; }
  .check-box { width: 19px; height: 19px; border: 1.5px solid #444; border-radius: 3px; }

  .gift-field { position: absolute; left: 540px; font-family: "Arimo", sans-serif; font-size: 19px; display: flex; align-items: flex-end; }
  .amount-box { width: 220px; height: 29px; border: 1px solid #444; border-radius: 3px; margin-left: 10px; }
  .gift-field .form-line { height: 17px; margin-left: 2px; }
</style>
</head>
<body>

<section class="envelope-front">
  <div class="front-backdrop" role="img" aria-label="Dark night sky photograph fading to a black mountain silhouette"></div>
  <div class="front-wordmark">
    <div class="church-name">VIDA NUEVA</div>
    <div class="church-sub">MISSION CHURCH</div>
  </div>
  <div class="front-contact">
    <div>418 Harbor View Ave. Austin, TX 78701</div>
    <div>www.Vidanuevatx.com<span class="divider-bar"></span>@VidaNuevaTX</div>
  </div>
</section>

<section class="envelope-back">
  <div class="back-frame"></div>
  <div class="back-header-rule"></div>
  <div class="back-column-rule"></div>

  <div class="back-wordmark">
    <div class="church-name">VIDA NUEVA</div>
    <div class="church-sub">MISSION CHURCH</div>
  </div>

  <p class="mission-statement">At Vida Nueva Mission Church you will find uplifting worship and inspiring messages. We are built on the mission to share a love of God through contribution to our community. We seek to help people build new lives and help them develop an unbreakable bond with God. Through service to each other and our community, we can create an environment that encourages growth, development, and faith.</p>

  <div class="donor-form">
    <div class="form-row" style="top:170px">Date <span class="form-line" style="width:164px"></span></div>
    <div class="form-row" style="top:214px">Name <span class="form-line" style="width:398px"></span></div>
    <div class="form-row" style="top:256px">Address <span class="form-line" style="width:382px"></span></div>
    <div class="form-row" style="top:302px; left:122px"><span class="form-line" style="width:382px"></span></div>
    <div class="form-row" style="top:342px">Email <span class="form-line" style="width:198px"></span>&nbsp;&nbsp;Phone <span class="form-line" style="width:148px"></span></div>
  </div>

  <div class="back-contact">
    <div>418 Harbor View Ave. Austin, TX 78701</div>
    <div>www.Vidanuevatx.com<span class="divider-bar"></span>@VidaNuevaTX</div>
  </div>

  <div class="ways-to-give">
    <div class="ways-title">WAYS TO GIVE</div>
    <div class="ways-sub">CASH OR CHECK WITH THIS ENVELOPE</div>
    <div class="ways-rule"></div>
  </div>

  <ul class="gift-options">
    <li><span class="check-box"></span>Tithe/Diezmo</li>
    <li><span class="check-box"></span>Offering/Ofrenda</li>
    <li><span class="check-box"></span>Missions/Misiones</li>
    <li><span class="check-box"></span>Building fund/Construcion</li>
    <li><span class="check-box"></span>Special offering/ofrenda especial</li>
  </ul>

  <div class="gift-field" style="top:369px; align-items:center">Amount <span class="amount-box"></span></div>
  <div class="gift-field" style="top:408px">Email : <span class="form-line" style="width:232px"></span></div>
  <div class="gift-field" style="top:434px">ZipCode : <span class="form-line" style="width:206px"></span></div>
</section>

</body>
</html>
```